TLR Property - Business Cards

Looking for a business card & general letterhead, signage etc design for our new logo.

Colours:
000a20
0056a2
00b5ef
0088ce
68cef2

Fonts:
Poppins
Karla

Please keep look and feel of new brand - example in the zip package I sent.

```html
<!DOCTYPE html>
<html lang="en">
<head>
<meta charset="utf-8">
<title>TLR Property – Business Cards</title>
<link rel="stylesheet" href="https://fonts.googleapis.com/css2?family=Poppins:wght@400;600;700&family=Karla:wght@400;500&display=swap">
<style>
  :root {
    --stage: #1c1c1e;
    --navy-deep: #000a20;
    --card-dark: #1a1e2b;
    --card-dark-2: #232838;
    --brand-blue: #0056a2;
    --bright-blue: #00b5ef;
    --mid-blue: #0088ce;
    --light-blue: #68cef2;
    --emboss: #3b404e;
    --text-light: #d7dbe3;
    --text-muted: #9aa1b0;
  }
  * { box-sizing: border-box; margin: 0; padding: 0; }
  html, body { width: 1200px; height: 852px; overflow: hidden; }
  body {
    background: var(--stage);
    font-family: "Karla", sans-serif;
    position: relative;
  }
  .card {
    position: absolute;
    width: 520px;
    height: 300px;
    border-radius: 22px;
    overflow: hidden;
    top: 276px;
  }

  /* Front */
  .card-front {
    left: 50px;
    background: linear-gradient(135deg, var(--card-dark-2), var(--card-dark) 60%, var(--navy-deep));
  }
  .front-wordmark {
    position: absolute;
    left: 0; right: 0; top: 100px;
    text-align: center;
    font-family: "Poppins", sans-serif;
    font-weight: 700;
    font-size: 46px;
    letter-spacing: 1px;
    color: var(--emboss);
  }
  .front-web {
    position: absolute;
    right: 30px; bottom: 34px;
    font-size: 11px;
    letter-spacing: 5px;
    color: var(--text-muted);
  }
  .front-strip {
    position: absolute;
    left: 0; right: 0; bottom: 0;
    height: 9px;
    background: var(--brand-blue);
  }

  /* Back */
  .card-back {
    left: 630px;
    background: linear-gradient(135deg, var(--card-dark-2), var(--card-dark));
  }
  .back-panel {
    position: absolute;
    left: 0; top: 0;
    width: 270px; height: 300px;
  }
  .back-wordmark {
    position: absolute;
    left: 28px; top: 128px;
    font-family: "Poppins", sans-serif;
    font-weight: 700;
    font-size: 30px;
    color: #ffffff;
  }
  .contact {
    position: absolute;
    left: 292px; top: 48px;
    color: var(--text-light);
  }
  .contact-name {
    font-family: "Poppins", sans-serif;
    font-weight: 600;
    font-size: 20px;
    color: var(--bright-blue);
    line-height: 1.1;
  }
  .contact-title {
    font-size: 10px;
    color: var(--text-muted);
    margin-bottom: 22px;
  }
  .contact-list { list-style: none; }
  .contact-list li {
    display: flex;
    align-items: center;
    gap: 10px;
    font-size: 12px;
    line-height: 1;
    margin-bottom: 9px;
  }
  .contact-list svg { width: 12px; height: 12px; flex: none; fill: var(--text-muted); }
  .contact-address { font-size: 12px; margin-top: 6px; }
</style>
</head>
<body>

  <section class="card card-front" aria-label="Business card front">
    <div class="front-wordmark">TLR Property</div>
    <div class="front-web">www.tlrproperty.com</div>
    <div class="front-strip"></div>
  </section>

  <section class="card card-back" aria-label="Business card back">
    <svg class="back-panel" viewBox="0 0 270 300" aria-hidden="true">
      <path d="M0 0 H172 Q262 150 244 300 H0 Z" fill="var(--mid-blue)"/>
      <path d="M0 0 H160 Q250 150 234 300 H0 Z" fill="var(--brand-blue)"/>
    </svg>
    <div class="back-wordmark">TLR Property</div>

    <div class="contact">
      <div class="contact-name">Marcus Hale</div>
      <div class="contact-title">Associate Director</div>
      <ul class="contact-list">
        <li>
          <svg viewBox="0 0 24 24"><path d="M6.6 10.8a15 15 0 0 0 6.6 6.6l2.2-2.2a1 1 0 0 1 1-.25 11 11 0 0 0 3.6.6 1 1 0 0 1 1 1V20a1 1 0 0 1-1 1A17 17 0 0 1 3 4a1 1 0 0 1 1-1h3.5a1 1 0 0 1 1 1c0 1.25.2 2.45.6 3.6a1 1 0 0 1-.25 1z"/></svg>
          555-010-0142
        </li>
        <li>
          <svg viewBox="0 0 24 24"><path d="M2 5h20v14H2z M2 5l10 8 10-8" fill="none" stroke="var(--text-muted)" stroke-width="2"/></svg>
          marcus@tlrproperty.com
        </li>
        <li>
          <svg viewBox="0 0 24 24"><circle cx="12" cy="12" r="10" fill="none" stroke="var(--text-muted)" stroke-width="2"/><path d="M2 12h20M12 2c3 3 3 17 0 20M12 2c-3 3-3 17 0 20" fill="none" stroke="var(--text-muted)" stroke-width="1.6"/></svg>
          www.tlrproperty.com
        </li>
      </ul>
      <div class="contact-address">27 Harbour Lane Westmead</div>
    </div>
  </section>

</body>
</html>
```